Digital Agency Needs a Relaunch

We are looking for a modern, top-notch design to elevate our brand to win new clients. It has to build on the clarity of message in the current wireframes and must fit together well on Wordpress.

The winning designer will need to complete the other pages, but please focus on the homepage as the base of your proposed designs for us.

Use the existing logo as a point, and the colour scheme should be around that, we currently use these colours, but you can suggest new mixes:
Purple: #5c306b
Orange: #e27927
Grey: #5f4f61
Light grey: #cacaca
Off white: #ececec
Blue: #674ea7
Updates

Need extra days to review

Target Market(s)

Decent Sized SME Businesses (20+ Staff, Over £1m turnover)

Industry/Entity Type

Digital Marketing

Number of Pages Required

5+ page

Font styles to use
Sans Serif

Colors

Designer to choose colors to be used in the design.

Requirements
Must have
• A real attention on the design piece. Ignore the current website and really focus on the messaging and the brief.
Nice to have
• Read the messages and think about the impact. Use the purple in the logo more than the orange, but try to keep it smart rather than cool
Should not have
• Inconsistent design, serif fonts, stock images and not meeting the wireframes.

```html
<!DOCTYPE html>
<html lang="en">
<head>
<meta charset="utf-8">
<title>Vanto Digital – Growth works for you</title>
<link rel="stylesheet" href="https://fonts.googleapis.com/css2?family=Poppins:wght@300;400;500;600&display=swap">
<style>
:root{
  --purple:#5c306b;
  --violet:#674ea7;
  --violet-mid:#6a52ab;
  --deep:#3c2a68;
  --orange:#e27927;
  --grey:#5f4f61;
  --light-grey:#cacaca;
  --off-white:#ececec;
  --ink:#1d1d1f;
  --white:#ffffff;
}
*{box-sizing:border-box;margin:0;padding:0}
html,body{width:1200px;height:4539px;overflow:hidden}
body{font-family:'Poppins',sans-serif;color:var(--ink);background:var(--white);position:relative}
section,header,footer{position:relative;width:1200px}
.abs{position:absolute}

/* header */
.site-header{height:120px;background:var(--white)}
.brand{left:74px;top:30px;display:flex;align-items:center;gap:10px;font-size:30px;font-weight:400;color:var(--grey)}
.brand-dot{width:14px;height:14px;border-radius:50%;background:var(--grey)}
.util-nav{right:66px;top:29px;display:flex;gap:0;font-size:11px;color:var(--ink)}
.util-nav span{padding:0 19px;border-left:1px solid var(--light-grey)}
.util-nav span:first-child{border-left:none}
.main-nav{right:66px;top:69px;display:flex;gap:56px;font-size:13px;font-weight:500}

/* hero */
.hero{height:585px;background:linear-gradient(135deg,#3b2a6b 0%,#4a2c72 45%,#3a2a66 100%);overflow:hidden}
.hero-art{left:140px;top:50px;width:920px;height:535px;background:radial-gradient(ellipse at 50% 60%,rgba(190,70,60,.55),rgba(20,90,140,.45) 45%,rgba(59,42,107,0) 75%)}
.hero-title{left:0;width:1200px;top:222px;text-align:center;font-size:52px;font-weight:500;line-height:72px;color:var(--white);text-shadow:0 3px 8px rgba(0,0,0,.35)}
.hero-title em{font-style:normal;color:#d9b8f0}

/* intro */
.intro{height:583px}
.intro h2{left:0;width:1200px;text-align:center;top:84px;font-size:40px;font-weight:400;line-height:60px}
.intro h2 .accent{display:block;color:var(--purple)}
.pillar{width:305px;font-size:16px;line-height:25px;color:var(--ink);top:278px}
.pillar svg{display:block;margin-bottom:18px}
.pillar b{font-weight:400;color:var(--violet)}

/* band */
.band{height:99px;background:linear-gradient(90deg,var(--purple),var(--violet))}
.band-text{left:122px;top:35px;font-size:24px;color:var(--white);font-weight:400}
.btn{background:var(--white);color:var(--ink);border-radius:4px;display:flex;align-items:center;justify-content:center;gap:12px;font-size:19px}
.band .btn{left:927px;top:21px;width:188px;height:57px}

/* services */
.services{height:484px;background:var(--off-white)}
.svc{top:58px;width:254px;height:366px;background:var(--white);border-radius:14px;padding:40px 28px}
.svc h3{font-size:23px;font-weight:500;margin:92px 0 12px}
.svc li{list-style:none;font-size:15px;line-height:31px;color:var(--grey)}

/* why */
.why{height:668px;background:var(--violet-mid);color:var(--white)}
.sprout{left:550px;top:50px;width:110px;height:105px;border-radius:6px;background:linear-gradient(180deg,#6a52ab 0%,#4f8a3a 45%,#4a2e22 80%,var(--orange) 100%)}
.why h2{left:0;width:1200px;text-align:center;top:178px;font-size:52px;font-weight:500}
.why h2 span{color:#b7a8d8}
.reason{top:318px;width:262px;font-size:14.5px;line-height:23px}
.reason svg{display:block;margin-bottom:28px}
.why-bar{left:44px;top:578px;width:1115px;height:90px;background:#5f4699;display:flex;align-items:center;justify-content:center;font-size:20px}

/* case studies */
.cases{height:673px}
.cases h2{left:0;width:1200px;text-align:center;top:82px;font-size:40px;font-weight:500;line-height:46px;color:var(--violet)}
.cases h2 span{display:block;color:var(--purple);font-weight:600}
.case-card{top:254px;width:252px;height:305px;border:1px solid #e2dce8;border-radius:14px;background:var(--white)}
.case-card.raised{box-shadow:0 16px 30px rgba(0,0,0,.12);border-color:transparent}
.learn{position:absolute;left:0;right:0;bottom:26px;display:flex;justify-content:center;align-items:center;gap:8px;font-size:16px;color:var(--violet)}

/* blog */
.blog{height:640px;background:var(--off-white)}
.blog h2{left:0;width:1200px;text-align:center;top:55px;font-size:42px;font-weight:500;color:var(--purple)}
.post{top:146px;width:252px}
.post-img{height:307px;background:var(--white);border-radius:14px}
.post h3{margin-top:20px;width:236px;font-size:19px;font-weight:400;line-height:24px}

/* cta */
.cta{height:98px;background:linear-gradient(90deg,var(--purple),var(--violet))}
.cta-text{left:122px;top:33px;font-size:23px;font-weight:500;color:var(--white)}
.cta .btn{left:855px;top:20px;width:260px;height:58px}

/* footer */
.site-footer{height:589px;background:var(--deep);color:#a99ac9}
.fcol{font-size:16px;line-height:31px}
.fcol h4{font-size:18px;font-weight:500;color:var(--white);margin-bottom:2px}
.contact-row{display:flex;gap:12px;align-items:flex-start;line-height:20px;margin-top:14px}
.footer-base{left:44px;top:522px;width:1115px;border-top:1px solid #5a4887;padding-top:18px;display:flex;font-size:12px}
.footer-base .legal{margin-left:auto;display:flex;gap:88px;padding-right:40px}
</style>
</head>
<body>

<header class="site-header">
  <div class="abs brand"><span class="brand-dot"></span>Vanto Digital</div>
  <nav class="abs util-nav"><span>Blog</span><span>About Us</span><span>Contact Us</span><span>01234 567 890</span></nav>
  <nav class="abs main-nav"><span>Create</span><span>Communicate</span><span>Convert</span><span>Close</span><span>Case Studies</span></nav>
</header>

<section class="hero">
  <div class="abs hero-art" role="img" aria-label="Illustration of coloured upward arrows rising at different heights"></div>
  <h1 class="abs hero-title">Growth works for you<br><em>in your targeting</em></h1>
</section>

<section class="intro">
  <h2 class="abs">Fed Up With Agencies Who Don’t Care?<span class="accent">We’ve Heard That Before</span></h2>
  <div class="abs pillar" style="left:67px">
    <svg width="56" height="56" viewBox="0 0 56 56" fill="none" stroke="#1d1d1f" stroke-width="2"><circle cx="22" cy="16" r="10"/><path d="M4 50c0-12 8-20 18-20 5 0 9 2 12 5"/><path d="M42 34l3 6 6 1-4 4 1 6-6-3-6 3 1-6-4-4 6-1z"/></svg>
    <p><b>We know every client has unique needs.</b> Yet, few digital agencies spend enough time getting to know the clients Business</p>
  </div>
  <div class="abs pillar" style="left:428px">
    <svg width="56" height="56" viewBox="0 0 56 56" fill="none" stroke="#1d1d1f" stroke-width="2"><path d="M32 8l4 12 12 4-12 4-4 12-4-12-12-4 12-4z"/><path d="M12 4l2 6 6 2-6 2-2 6-2-6-6-2 6-2z"/><path d="M12 36l2 5 5 2-5 2-2 5-2-5-5-2 5-2z"/></svg>
    <p><b>We’re different.</b> We take a highly personalised approach to every project, working closely with our clients to understand their objectives, challenges and target audience</p>
  </div>
  <div class="abs pillar" style="left:788px">
    <svg width="56" height="56" viewBox="0 0 56 56" fill="none" stroke="#1d1d1f" stroke-width="2"><circle cx="28" cy="12" r="9"/><path d="M24 12l3 3 6-6"/><circle cx="16" cy="30" r="6"/><circle cx="40" cy="30" r="6"/><path d="M4 52c0-8 5-14 12-14s12 6 12 14M28 52c0-8 5-14 12-14s12 6 12 14"/></svg>
    <p><b>Knowing your business</b> is the first step in helping you grow. It’s how we work, and it will work for you.</p>
  </div>
</section>

<section class="band">
  <p class="abs band-text">Achieve Growth That Works</p>
  <div class="abs btn"><svg width="16" height="16" viewBox="0 0 24 24" fill="none" stroke="#1d1d1f" stroke-width="2"><path d="M5 3h4l2 5-3 2a12 12 0 006 6l2-3 5 2v4a2 2 0 01-2 2A18 18 0 013 5a2 2 0 012-2z"/></svg>Set Up A Call</div>
</section>

<section class="services">
  <div class="abs svc" style="left:67px">
    <svg width="40" height="40" viewBox="0 0 40 40" fill="none" stroke="#1d1d1f" stroke-width="2"><rect x="4" y="8" width="26" height="28"/><path d="M16 24l18-18 4 4-18 18h-4z"/></svg>
    <h3>Create</h3><ul><li>Branding</li><li>Graphics</li><li>Video</li><li>Content</li></ul>
  </div>
  <div class="abs svc" style="left:338px">
    <svg width="40" height="40" viewBox="0 0 40 40" fill="none" stroke="#1d1d1f" stroke-width="2"><rect x="4" y="3" width="26" height="9" rx="2"/><rect x="8" y="15" width="26" height="9" rx="2"/><rect x="4" y="27" width="30" height="9" rx="2"/></svg>
    <h3>Communicate</h3><ul><li>Ads</li><li>Social</li><li>Organic</li><li>Email</li></ul>
  </div>
  <div class="abs svc" style="left:608px">
    <svg width="40" height="40" viewBox="0 0 40 40" fill="none" stroke="#1d1d1f" stroke-width="2"><circle cx="20" cy="20" r="5"/><path d="M20 3v10M20 27v10M3 20h10M27 20h10M8 8l7 7M25 25l7 7M32 8l-7 7M15 25l-7 7"/></svg>
    <h3 style="margin-top:88px">Convert</h3><ul><li>Websites</li><li>E-Commerce</li><li>Analytics</li><li>Lead Generation</li></ul>
  </div>
  <div class="abs svc" style="left:879px">
    <svg width="44" height="40" viewBox="0 0 44 40" fill="none" stroke="#1d1d1f" stroke-width="2"><path d="M2 12l8-4 8 4 8-4 8 4 8-4"/><path d="M10 18l10 10c2 2 5 2 6 0l8-8M14 14l6 4 6-4"/></svg>
    <h3 style="margin-top:88px">Close</h3><ul><li>CRM</li><li>Systems</li><li>Customer Success</li><li>AI &amp; Automations</li></ul>
  </div>
</section>

<section class="why">
  <div class="abs sprout" role="img" aria-label="Illustration of a green seedling growing from a mound of soil"></div>
  <h2 class="abs"><span>Vanto</span> Where Growth Works</h2>
  <div class="abs reason" style="left:102px">
    <svg width="38" height="34" viewBox="0 0 38 34" fill="none" stroke="#d8cff0" stroke-width="2"><rect x="6" y="3" width="26" height="20"/><path d="M2 28h22"/><rect x="24" y="12" width="12" height="20"/></svg>
    <p>We understand the importance of a strong online presence. That’s why we offer a complete range of digital marketing solutions to help your reach your growth goals.</p>
  </div>
  <div class="abs reason" style="left:449px">
    <svg width="34" height="38" viewBox="0 0 34 38" fill="none" stroke="#d8cff0" stroke-width="2"><path d="M17 3l13 5v12c0 8-6 13-13 16C10 33 4 28 4 20V8z"/><path d="M11 19l4 4 8-8"/></svg>
    <p>Our track record demostrates expertise in all forms of digital marketing, including Website builds, Seekora Ads, SEO, Email Marketing.</p>
  </div>
  <div class="abs reason" style="left:826px">
    <svg width="36" height="38" viewBox="0 0 36 38" fill="none" stroke="#d8cff0" stroke-width="2"><rect x="3" y="7" width="30" height="28"/><path d="M3 15h30M11 3v8M25 3v8M12 25l4 4 8-8"/></svg>
    <p>We’re constantly staying up-to-date on the latest trends, tech and best practices in the industry, so you can trust that you’re getting the most effective and efficient stragies for your business growth.</p>
  </div>
  <div class="abs why-bar">Set up a call and we’re confident we can show you where we can add growth and value to your business.</div>
</section>

<section class="cases">
  <h2 class="abs">Create<span>Case Studies</span></h2>
  <div class="abs case-card" style="left:78px"><span class="learn">Learn More <svg width="16" height="14" viewBox="0 0 16 14" fill="none" stroke="#e27927" stroke-width="2"><path d="M1 7h13M9 2l5 5-5 5"/></svg></span></div>
  <div class="abs case-card" style="left:342px"><span class="learn">Learn More <svg width="16" height="14" viewBox="0 0 16 14" fill="none" stroke="#e27927" stroke-width="2"><path d="M1 7h13M9 2l5 5-5 5"/></svg></span></div>
  <div class="abs case-card raised" style="left:606px"><span class="learn">Learn More <svg width="16" height="14" viewBox="0 0 16 14" fill="none" stroke="#e27927" stroke-width="2"><path d="M1 7h13M9 2l5 5-5 5"/></svg></span></div>
  <div class="abs case-card" style="left:870px"><span class="learn">Learn More <svg width="16" height="14" viewBox="0 0 16 14" fill="none" stroke="#e27927" stroke-width="2"><path d="M1 7h13M9 2l5 5-5 5"/></svg></span></div>
</section>

<section class="blog">
  <h2 class="abs">From the Blog</h2>
  <article class="abs post" style="left:76px"><div class="post-img"></div><h3>Seekora’s New PPC Features are Loaded with AI</h3></article>
  <article class="abs post" style="left:340px"><div class="post-img"></div><h3>How Seekora Killed the Broad Match Keyword?</h3></article>
  <article class="abs post" style="left:603px"><div class="post-img"></div><h3>The 9 Rules of Social Media Engagement (Part II)</h3></article>
  <article class="abs post" style="left:867px"><div class="post-img"></div><h3>The 9 Rules of Social Media Engagement (Part I)</h3></article>
</section>

<section class="cta">
  <p class="abs cta-text">We’re The Turbo Boost For Your Digital Marketing Engine</p>
  <div class="abs btn">Put Your Foot Down <svg width="16" height="16" viewBox="0 0 24 24" fill="none" stroke="#1d1d1f" stroke-width="2"><path d="M22 2L11 13M22 2l-7 20-4-9-9-4z"/></svg></div>
</section>

<footer class="site-footer">
  <div class="abs fcol" style="left:74px;top:80px"><h4>Create</h4><p>Branding</p><p>Graphics</p><p>Video</p><p>Content</p></div>
  <div class="abs fcol" style="left:326px;top:80px"><h4>Convert</h4><p>Websites</p><p>Lead Generation</p><p>Ecommerce</p><p>Analytics</p></div>
  <div class="abs fcol" style="left:573px;top:80px"><h4>Connect</h4><p>Case Studies</p><p>Blog</p><p>About Us</p></div>
  <div class="abs fcol" style="left:803px;top:80px;width:320px"><h4>Contact</h4>
    <div class="contact-row"><svg width="16" height="16" viewBox="0 0 24 24" fill="none" stroke="#a99ac9" stroke-width="2"><path d="M5 3h4l2 5-3 2a12 12 0 006 6l2-3 5 2v4a2 2 0 01-2 2A18 18 0 013 5a2 2 0 012-2z"/></svg>01234 567 890</div>
    <div class="contact-row" style="margin-top:34px"><svg width="16" height="18" viewBox="0 0 24 26" fill="none" stroke="#a99ac9" stroke-width="2"><path d="M12 24s8-8 8-14a8 8 0 00-16 0c0 6 8 14 8 14z"/><circle cx="12" cy="10" r="3"/></svg><span>Harbour Point House, Kestrel<br>Berkshire KB1 2AB</span></div>
  </div>
  <div class="abs fcol" style="left:74px;top:322px"><h4>Communicate</h4><p>Ads</p><p>Organic</p><p>Social</p><p>Email</p></div>
  <div class="abs fcol" style="left:326px;top:322px"><h4>Close</h4><p>CRM</p><p>Systems</p><p>Customer Success</p><p>AI &amp; Automations</p></div>
  <div class="abs footer-base"><span>(c) Vanto Digital Limited. All rights reserved</span><span class="legal"><span>Sitemap</span><span>Terms of Use</span><span>Privacy Policy</span></span></div>
</footer>

</body>
</html>
```